Book Cover for a book on Lantern Road Ventures

I am self-publishing my book on Brindlemark and need a book cover made. Below are the details. See attached templates for size we need to use. I also attached a previous cover we had made that I liked. The problem with it was they were two boys helping each other but the book is about women. I'm open to your ideas on the cover though, but I wanted to show you a style I liked as an idea.
Front of Cover
Book Title: Lantern Road Ventures
Book Subtitle: Loose Pages of a Harbor Keeper
Author Name: Mirela T. Dunbar
Add on the Spine of Cover: Lantern Road Ventures and Mirela T. Dunbar
Back of the Cover Text:
Lantern Road Ventures: Loose Pages of a Harbor Keeper is an honest account of a business owner’s experience attempting to navigate the start-up community while also pursuing spiritual growth. Author Mirela Dunbar defines a spiritual entrepreneur as “someone who runs an enterprise with the purpose of growing love rather than material gain.” This book discusses the three dimensions of Lantern Road Ventures:
1. The business is an integral part of the founder’s spiritual journey.
2. Employees working for the spiritual enterprise, whether they know it or not, encounter this company because it's part of their spiritual path.
3. The business itself has a life force of its own and its purpose is to further the kingdom of heaven on earth.
These three dimensions happen simultaneously and work together to produce the greatest possible result. However, this can feel confusing to a founder juggling these dimensions while also trying to manage and run a business. This is not a formulaic self-help book or roadmap. Rather, it is a compilation of personal reflections that often seem at odds with the traditional world of entrepreneurship.
Below the description add my picture (see attached for my picture)
Bio text:
Mirela Dunbar founded Calveta with the vision of ushering in a life-long education system that shifts away from standardization to one that empowers people to live their purpose. In college, Mirela interned for Open Kettle, a women’s empowerment initiative where she recognized her passion for helping people find their voice. Mirela's 20-year journey has come full circle to empowering other female CEOs who are pursuing the path of Lantern Road Ventures.
NOTE: Please note that Brindlemark puts a bar code on the bottom right of the back cover as is noted on the attached template.
Size template is attached to the brief, here are the sizes typed out:
# Description Width (in) Height (in)
1 Full Cover 12.79 9.25
2 Front Cover 6 9
3 Safe Area 5.875 8.75
4 Bleed 0.125 0.125
5 Margin 0.125 0.125
6 Spine 0.54 9
7 Spine Safe Area 0.415 8.75
8 Spine Margin 0.062 0.062
9 Barcode Margin 0.25 0.25
Pre-publication checklist
BRINDLEMARK TIPS for the final cover:
1. Save as a PDF. Your cover must be a single PDF that includes the back cover, spine, and front cover as one image.
2. Flatten all transparencies. These can cause the file to print with missing or distorted content. Consult your software's documentation to learn how.
3. Embed your fonts. Consult your software's documentation to learn how.
4. Remove crop marks, color bars, template text. Crop marks are lines showing where pages should be trimmed. Color bars are strips with a series of patches used to ensure color balance during printing. Also, remove any template text, PDF creation guides, or software references.
5. Ensure your cover image meets the minimum resolution of 300 DPI (dots per inch).
6. Optimize PDFs. Optimization is useful to reduce your file size, allowing for higher performance when transferring, uploading, viewing, and printing the files.
7. Remove file security. Locked or encrypted files will fail review.
Target Market(s)
Women who want to be CEOs or are currently CEOs of companies.
Industry/Entity Type
Entrepreneurship, business, spirituality
Requirements
Must have
- Just the text on the description. A very welcoming feel.
Nice to have
- I like the idea of having a sunrise/sunset in the image somehow like in the example I attached to the brief, but again I'm open.
Should not have
- Please don't put any yoga or meditation poses or hands outstretched. I have a lot of interesting ones that look like my example so if you are going to submit after Saturday 10/29, please only do so if you have a new idea! Thanks!

```html
<!DOCTYPE html>
<html lang="en">
<head>
<meta charset="utf-8">
<title>Lantern Road Ventures — Book Cover</title>
<link rel="stylesheet" href="https://fonts.googleapis.com/css2?family=Libre+Baskerville:wght@400;700&display=swap">
<style>
  :root {
    --back-bg: #000000;
    --spine-bg: #1c1c1c;
    --body-text: #f0f0f0;
    --title-gold: #f3e2b8;
    --cream: #f6e8c8;
    --subtitle: #f3dfc4;
    --sky-top: #f0b878;
    --sky-mid: #ee8c52;
    --horizon: #b8603e;
    --sea-mid: #56494a;
    --sea-deep: #2a2d35;
  }
  * { margin: 0; padding: 0; box-sizing: border-box; }
  html, body { width: 1200px; height: 868px; overflow: hidden; background: var(--back-bg); }
  .cover { position: relative; width: 1200px; height: 868px; display: flex; }

  .back-cover {
    width: 575px; height: 868px; background: var(--back-bg);
    color: var(--body-text); font-family: "Libre Baskerville", Georgia, serif;
    font-size: 11.6px; line-height: 20px; padding: 46px 40px 0 30px; text-align: justify;
  }
  .back-title { color: var(--title-gold); font-weight: 700; font-size: 13.4px; }
  .blurb-intro { text-align: center; }
  .dimensions { list-style: disc; margin: 14px 0 16px 24px; text-align: left; }
  .dimensions li { padding-left: 2px; }
  .bio { display: flex; gap: 15px; margin-top: 46px; }
  .author-photo {
    flex: 0 0 97px; height: 91px;
    background: linear-gradient(160deg, #7ea65a 0%, #5d8a3f 45%, #c94a6a 75%, #d8566f 100%);
  }
  .bio-text { flex: 1; margin-top: -4px; }

  .spine {
    width: 52px; height: 868px; background: var(--spine-bg);
    position: relative; color: var(--cream); font-family: "Libre Baskerville", Georgia, serif;
  }
  .spine-title, .spine-author {
    position: absolute; left: 50%; writing-mode: vertical-rl; transform: translateX(-50%);
    white-space: nowrap;
  }
  .spine-title { top: 163px; font-size: 16px; letter-spacing: 1px; }
  .spine-author { top: 658px; font-size: 15px; }

  .front-cover {
    width: 573px; height: 868px; position: relative;
    font-family: "Libre Baskerville", Georgia, serif; text-align: center;
  }
  .front-photo {
    position: absolute; inset: 0;
    background: linear-gradient(180deg, var(--sky-top) 0%, #f2b270 22%, var(--sky-mid) 38%, var(--horizon) 48%, var(--sea-mid) 60%, #3c3a40 76%, var(--sea-deep) 100%);
  }
  .front-title {
    position: absolute; top: 378px; left: 0; right: 0;
    color: var(--cream); font-size: 42px; line-height: 76px; letter-spacing: 1.5px; font-weight: 400;
  }
  .front-subtitle {
    position: absolute; top: 612px; left: 0; right: 0;
    color: var(--subtitle); font-weight: 700; font-size: 17.5px;
  }
  .front-author {
    position: absolute; top: 793px; left: 0; right: 0;
    color: var(--subtitle); font-size: 23px;
  }
</style>
</head>
<body>
<main class="cover">
  <section class="back-cover">
    <p class="blurb-intro"><span class="back-title">LANTERN ROAD VENTURES:</span> <strong class="back-title">Loose Pages of a Harbor Keeper</strong> is an honest account of a business owner’s experience attempting to navigate the start-up community while also pursuing spiritual growth. Author Mirela Dunbar defines a spiritual entrepreneur as “someone who runs an enterprise with the purpose of growing love rather than material gain.” This book discusses the three dimensions of Lantern Road Ventures:</p>
    <ul class="dimensions">
      <li>The business is an integral part of the founder’s spiritual journey.</li>
      <li>Employees working for the spiritual enterprise, whether they know it or not, encounter this company because it’s part of their spiritual path.</li>
      <li>The business itself has a life force of its own and its purpose is to further the kingdom of heaven on earth.</li>
    </ul>
    <p class="blurb">These three dimensions happen simultaneously and work together to produce the greatest possible result. However, this can feel confusing to a founder juggling these dimensions while also trying to manage and run a business. This is not a formulaic self-help book or roadmap. Rather, it is a compilation of personal reflections that often seem at odds with the traditional world of entrepreneurship.</p>
    <div class="bio">
      <div class="author-photo" role="img" aria-label="Portrait photo of the author outdoors"></div>
      <p class="bio-text">Mirela Dunbar founded Calveta with the vision of ushering in a life-long education system that shifts away from standardization to one that empowers people to live their purpose. In college, Mirela interned for Open Kettle, a women’s empowerment initiative where she recognized her passion for helping people find their voice. Mirela’s 20-year journey has come full circle to empowering other female CEOs who are pursuing the path of Lantern Road Ventures.</p>
    </div>
  </section>

  <aside class="spine">
    <span class="spine-title">LANTERN ROAD VENTURES</span>
    <span class="spine-author">Mirela T. Dunbar</span>
  </aside>

  <section class="front-cover">
    <div class="front-photo" role="img" aria-label="Photo of a sunset over ocean waves"></div>
    <h1 class="front-title">LANTERN ROAD<br>VENTURES</h1>
    <p class="front-subtitle">Loose Pages of a Harbor Keeper</p>
    <p class="front-author">Mirela T. Dunbar</p>
  </section>
</main>
</body>
</html>
```